Christmas Candle Label

We require a Christmas candle label that fits with our current brand (see larkfieldcandleworks.com.au, and also example attached). On the attached we would like the word 'Marlowe - Pendleby' replaced with 'Merry Christmas' (or something creative that you can come up with) and the writing on the left hand side 'lose yourself in the subtle.........' replaced with 'its beginning to smell a lot like Christmas' (or something creative that you can come up with). We would like the flora image in the background replaced with a line drawing of a Christmas tree or holy or anything else that is appropriate. Finally we are not sure if a different colour label i.e. red, maroon or green (with lots of black, silver or gold writing) instead of black would be best for this label. It may be best to see a comparison of our original black label with black, silver or gold writing, and the other colours.

```html
<!DOCTYPE html>
<html lang="en">
<head>
<meta charset="UTF-8">
<title>Christmas Candle Label</title>
<link rel="stylesheet" href="https://fonts.googleapis.com/css2?family=Montserrat:wght@400;500&family=Merriweather:wght@400&display=swap">
<style>
  :root {
    --page-bg: #ece6e7;
    --label-black: #1c1c1d;
    --label-edge: #2a2a2b;
    --text-white: #f3f1ee;
    --text-cream: #f1e6b2;
    --text-muted: #b9b6b0;
    --gold-light: #f4e3a1;
    --gold-mid: #c9a851;
    --gold-deep: #7a6124;
  }
  * { box-sizing: border-box; margin: 0; padding: 0; }
  html, body {
    width: 1200px;
    height: 900px;
    overflow: hidden;
    background: var(--page-bg);
  }
  .canvas {
    width: 1200px;
    height: 900px;
    display: flex;
    align-items: center;
    justify-content: center;
  }
  .label {
    width: 1100px;
    height: 400px;
    background: var(--label-black);
    display: grid;
    grid-template-columns: 270px 250px 580px;
  }
  .panel {
    position: relative;
    padding: 40px 36px;
  }
  .panel + .panel { border-left: 1px solid var(--label-edge); }

  .quote-panel {
    display: flex;
    align-items: center;
  }
  .quote-text {
    font-family: "Merriweather", Georgia, serif;
    font-size: 23px;
    line-height: 1.36;
    color: var(--text-white);
  }

  .care-panel {
    display: flex;
    flex-direction: column;
    justify-content: center;
    gap: 14px;
  }
  .care-title {
    font-family: "Montserrat", Arial, sans-serif;
    font-weight: 500;
    font-size: 14px;
    letter-spacing: 0.12em;
    text-transform: uppercase;
    color: var(--text-white);
  }
  .care-text {
    font-family: "Montserrat", Arial, sans-serif;
    font-size: 12px;
    line-height: 1.6;
    color: var(--text-muted);
  }

  .front-panel { padding: 44px 44px; }
  .fragrance-name {
    font-family: "Montserrat", Arial, sans-serif;
    font-weight: 500;
    font-size: 24px;
    line-height: 1.2;
    color: var(--text-white);
    max-width: 300px;
  }
  .headline {
    position: absolute;
    left: 44px;
    top: 170px;
    font-family: "Merriweather", Georgia, serif;
    font-size: 32px;
    line-height: 1.3;
    color: var(--text-cream);
  }
  .origin-line {
    position: absolute;
    left: 44px;
    bottom: 34px;
    font-family: "Montserrat", Arial, sans-serif;
    font-size: 12px;
    color: var(--text-white);
  }
  .tree-art {
    position: absolute;
    right: 56px;
    top: 50px;
    width: 140px;
    height: 290px;
    border-radius: 6px;
    background: radial-gradient(ellipse at 50% 55%, var(--gold-light) 0%, var(--gold-mid) 35%, var(--gold-deep) 65%, var(--label-black) 100%);
  }
</style>
</head>
<body>
  <main class="canvas">
    <section class="label">
      <div class="panel quote-panel">
        <p class="quote-text">“Breathe in the essence of Christmas as the scent of the season fills the air, bringing its magic to life.”</p>
      </div>

      <div class="panel care-panel">
        <h2 class="care-title">Candle Care</h2>
        <p class="care-text">Burn for 2–3 hours at a time. Trim wick to 5mm before lighting.</p>
        <p class="care-text">Never leave a burning candle unattended. Keep away from children and pets.</p>
      </div>

      <div class="panel front-panel">
        <h1 class="fragrance-name">Windswept Highland<br>Heath</h1>
        <p class="headline">The fragrance<br>of Christmas<br>is here.</p>
        <div class="tree-art" role="img" aria-label="Gold line-drawn swirl Christmas tree topped with a sparkling star"></div>
        <p class="origin-line">Handcrafted In Southern Tasmania</p>
      </div>
    </section>
  </main>
</body>
</html>
```